Game, Voice & Dedicated Server Company Needs a Business Card Design

We need a new business card design, centered around our new logo (PSD provided below).

Designs that we do like:
https://pixelmarsh.net/item/corporate-business-card/5382017?s_rank=43 (needs to be made more eye catching)

Our main areas of business are:
- Dedicated Servers
- Game Servers
- Voice Servers
- Mitigation Security Specialists

Industry/Entity Type

Business

Contact Information for Business Card

On the card: (and anything else you would suggest)
- Staff member name
- Staff member position in company
- Staff member phone number
- Staff member email
- Other / Staff member Chat ID
- Website link

Colors
9bcb3c
abd036

Requirements
Must have
• Design of Card:
• - Green (same green as the logo)
• - Business / Corporate design
• - Something a little different / abstract that shouts premium

```html
<!DOCTYPE html>
<html lang="en">
<head>
<meta charset="utf-8">
<title>Bramwick – Business Card</title>
<link rel="stylesheet" href="https://fonts.googleapis.com/css2?family=Arimo:ital,wght@0,400;0,700;1,700&display=swap">
<style>
  :root {
    --green: #8eff00;
    --slate: #3f4b4c;
    --white: #ffffff;
    --paper: #ffffff;
  }
  * { margin: 0; padding: 0; box-sizing: border-box; }
  html, body {
    width: 853px; height: 1200px; overflow: hidden;
    background: var(--paper);
    font-family: "Arimo", Arial, sans-serif;
  }
  .canvas { position: relative; width: 853px; height: 1200px; }

  /* Front side */
  .card-front {
    position: absolute; left: 3px; top: 8px; width: 849px; height: 480px;
    background: var(--green); overflow: hidden;
  }
  .stripe { position: absolute; left: 0; width: 100%; background: var(--slate); }
  .stripe--1 { top: 0; height: 8px; }
  .stripe--2 { top: 39px; height: 15px; }
  .stripe--3 { top: 81px; height: 28px; }
  .stripe--4 { top: 131px; height: 194px; }
  .stripe--5 { top: 348px; height: 27px; }
  .stripe--6 { top: 403px; height: 14px; }
  .stripe--7 { top: 447px; height: 10px; }

  .brand { position: absolute; display: flex; align-items: center; color: var(--green); font-weight: 700; }
  .brand__mark { background: var(--green); flex: none; }
  .brand__name { line-height: 1; letter-spacing: 1px; text-transform: uppercase; white-space: nowrap; }

  .brand--front { left: 140px; top: 175px; gap: 45px; }
  .brand--front .brand__mark { width: 130px; height: 130px; }
  .brand--front .brand__name { font-size: 66px; }

  /* Back side */
  .card-back {
    position: absolute; left: 0; top: 711px; width: 853px; height: 489px;
    background: var(--slate); overflow: hidden;
  }
  .brand--back { left: 20px; top: 30px; gap: 26px; }
  .brand--back .brand__mark { width: 96px; height: 96px; }
  .brand--back .brand__name { font-size: 45px; }

  .staff { position: absolute; left: 58px; top: 203px; }
  .staff__name { color: var(--white); font-size: 26px; font-weight: 700; letter-spacing: 1.5px; }
  .staff__role { margin-top: 6px; color: var(--green); font-size: 12.5px; font-weight: 700; font-style: italic; }

  .contact-panel {
    position: absolute; left: 432px; top: 2px; width: 419px; height: 485px;
    background: var(--green);
  }
  .contact { position: absolute; left: 0; right: 0; height: 24px; }
  .contact__text {
    position: absolute; right: 76px; bottom: 7px;
    font-size: 17px; color: var(--slate); white-space: nowrap; letter-spacing: 0.3px;
  }
  .contact__rule {
    position: absolute; left: 37px; right: 30px; bottom: 0; height: 3px;
    background: var(--white); border-radius: 2px;
  }
  .contact__icon { position: absolute; right: 28px; bottom: 3px; width: 36px; height: 36px; }
  .contact--phone { top: 135px; }
  .contact--email { top: 200px; }
  .contact--chat  { top: 264px; }
  .contact--web   { top: 328px; }
</style>
</head>
<body>
<main class="canvas">

  <section class="card-front" aria-label="Business card front">
    <div class="stripe stripe--1"></div>
    <div class="stripe stripe--2"></div>
    <div class="stripe stripe--3"></div>
    <div class="stripe stripe--4"></div>
    <div class="stripe stripe--5"></div>
    <div class="stripe stripe--6"></div>
    <div class="stripe stripe--7"></div>
    <div class="brand brand--front">
      <span class="brand__mark"></span>
      <span class="brand__name">Bramwick</span>
    </div>
  </section>

  <section class="card-back" aria-label="Business card back">
    <div class="brand brand--back">
      <span class="brand__mark"></span>
      <span class="brand__name">Bramwick</span>
    </div>

    <div class="staff">
      <p class="staff__name">STAFF MEMBER NAME</p>
      <p class="staff__role">STAFF MEMBER POSITION IN COMPANY</p>
    </div>

    <div class="contact-panel">
      <div class="contact contact--phone">
        <span class="contact__text">STAFF MEMBER PHONE NUMBER</span>
        <span class="contact__rule"></span>
        <svg class="contact__icon" viewBox="0 0 36 36" aria-hidden="true">
          <path d="M6 4 L12 2 L16 10 L12 14 Q16 24 26 28 L30 24 L36 30 L32 34 Q18 36 8 22 Q2 12 6 4 Z" fill="var(--white)"/>
        </svg>
      </div>
      <div class="contact contact--email">
        <span class="contact__text">STAFF MEMBER EMAIL</span>
        <span class="contact__rule"></span>
        <svg class="contact__icon" viewBox="0 0 36 36" aria-hidden="true">
          <rect x="2" y="6" width="32" height="24" fill="none" stroke="var(--white)" stroke-width="3"/>
          <path d="M2 6 L18 20 L34 6 M2 30 L14 17 M34 30 L22 17" fill="none" stroke="var(--white)" stroke-width="3"/>
        </svg>
      </div>
      <div class="contact contact--chat">
        <span class="contact__text">OTHER / STAFF MEMBER CHAT ID</span>
        <span class="contact__rule"></span>
        <svg class="contact__icon" viewBox="0 0 36 36" aria-hidden="true">
          <circle cx="18" cy="18" r="16" fill="var(--white)"/>
        </svg>
      </div>
      <div class="contact contact--web">
        <span class="contact__text">WEBSITE</span>
        <span class="contact__rule"></span>
        <svg class="contact__icon" viewBox="0 0 36 36" aria-hidden="true">
          <g fill="none" stroke="var(--white)" stroke-width="2">
            <circle cx="18" cy="18" r="16"/>
            <ellipse cx="18" cy="18" rx="7" ry="16"/>
            <path d="M18 2 V34 M2 18 H34 M5 10 H31 M5 26 H31"/>
          </g>
        </svg>
      </div>
    </div>
  </section>

</main>
</body>
</html>
```